Dental Learning Allies Needs a Great Looking Sales Brochure!

Please help us design a brochure for our company, Dental Learning Allies, LLC to use for sales and prospecting!
It is our first brochure, and as we are a small company, we don't normally use them, but we have an upcoming meeting and need a GREAT looking brochure with a call to action!
In addition to a pdf print ready version of the file, we need to receive a version with editable pdf text fields.
Our original thought is a 1-page, 4-panel fold or Tri-fold brochure, but we are open to recommendations based on the content.
More about us: We are a small company specializing in education, motivational speaking and event services for dental practices both large and big dental groups. You can check out our website at https://dentallearningallies.example
I have uploaded our logo files, some images for consideration, and proposed text content for the brochure. Note - if you have the space to add our KRV MOTO provider approval we would like to. If you do use the KRV Moto logo, we need to follow their logo guidelines which are also attached.
Should you have any questions, please don't hesitate to ask!
Thank you for helping make us look great!!!!

Target Market(s)

Dental Support Organizations (DSO's)

Font styles to use
Serif
Sans Serif

Requirements
Must have
• Our company logo
• At least 1-2 photos
• Professional look and feel
• Text from uploaded word document for proposed copy
Nice to have
• KRV logo and language showing we are KRV MOTO provider

```html
<!DOCTYPE html>
<html lang="en">
<head>
<meta charset="utf-8">
<title>Dental Learning Allies – Tri-fold Brochure</title>
<link href="https://fonts.googleapis.com/css2?family=Open+Sans:ital,wght@0,400;0,600;0,700;1,400;1,600&family=Roboto+Slab:wght@700&display=swap" rel="stylesheet">
<style>
:root{
  --blue:#1b78c8;
  --blue-deep:#0d5aa6;
  --blue-light:#4aa0e6;
  --ink:#1e1e1e;
  --grey:#6d6e72;
  --paper:#ffffff;
  --paper-soft:#f1f2f4;
  --stage:#e4e4e4;
}
*{margin:0;padding:0;box-sizing:border-box}
html,body{width:840px;height:1200px;overflow:hidden;background:var(--stage)}
body{font-family:"Open Sans",Arial,sans-serif;color:var(--ink);position:relative}
.spread{position:absolute;left:30px;width:780px;height:580px;background:var(--paper);box-shadow:0 6px 18px rgba(0,0,0,.18);overflow:hidden}
.spread--outside{top:20px}
.spread--inside{top:610px}
.spread svg.bg{position:absolute;inset:0}
.abs{position:absolute}
.brand{display:flex;align-items:center;gap:7px;font-family:"Open Sans",Arial,sans-serif;font-weight:600;letter-spacing:.3px;white-space:nowrap}
.brand__mark{width:14px;height:14px;background:currentColor;flex:none}
.white{color:#fff}
.blue{color:var(--blue)}
.web{display:flex;flex-direction:column;align-items:center;gap:6px;font-size:11px;font-weight:700;letter-spacing:.4px}
.web svg{width:16px;height:16px}

/* outside: approval panel */
.approval{left:22px;top:130px;width:220px}
.approval__badge{display:flex;align-items:center;gap:8px;margin-bottom:14px;font-weight:700;font-size:20px;color:var(--ink)}
.approval__badge span.sq{width:28px;height:28px;background:var(--blue)}
.approval p{font-size:10.6px;line-height:1.55}

/* outside: contact panel */
.contact{left:260px;top:0;width:260px;text-align:center;color:#fff}
.contact .brand{justify-content:center;margin-top:44px;font-size:16px}
.contact__addr{font-size:9.5px;line-height:1.5;margin-top:18px}
.contact__addr svg{width:13px;height:13px;display:block;margin:0 auto 4px}
.person{margin-top:16px}
.person__photo{width:54px;height:54px;border-radius:50%;margin:0 auto 6px;border:2px solid #fff;background:radial-gradient(circle at 50% 40%,#d8d2cc,#8a8f96)}
.person__name{font-size:10px;font-weight:700}
.person__line{font-size:9px;line-height:1.5}
.contact__web{position:absolute;left:0;right:0;top:500px}

/* outside: cover */
.cover__title{left:548px;top:70px;width:210px;font-family:"Roboto Slab",Georgia,serif;font-size:17px;line-height:1.22;color:var(--blue);text-transform:uppercase;text-align:center}
.cover__brand{left:560px;top:440px;font-size:15px}

/* inside */
.services{left:26px;top:70px;width:220px}
h2{font-family:"Open Sans",Arial,sans-serif;font-weight:600;font-size:17px;margin-bottom:8px}
.ticks{list-style:none}
.ticks li{position:relative;padding-left:18px;font-size:11px;line-height:1.35;margin-bottom:4px}
.ticks li::before{content:"";position:absolute;left:2px;top:3px;width:5px;height:9px;border:solid var(--blue);border-width:0 2px 2px 0;transform:rotate(40deg)}
.why{left:284px;top:40px;width:220px}
.why__lead{font-size:11px;margin-bottom:6px}
.why .ticks li{margin-bottom:5px}
.why__cta{margin-top:8px;font-size:12px;font-style:italic;color:var(--blue);line-height:1.35}
.quote{left:548px;top:48px;width:210px;border:1.5px solid var(--ink);padding:16px 14px 12px;font-size:10.2px;line-height:1.5}
.quote__mark{position:absolute;font-family:"Roboto Slab",Georgia,serif;font-size:30px;line-height:1}
.quote__mark--open{left:-4px;top:-12px;background:var(--paper);padding:0 3px}
.quote__mark--close{right:-4px;bottom:-20px;background:var(--paper);padding:0 3px}
.quote__cite{left:560px;top:232px;width:198px;text-align:right;font-size:9.5px;line-height:1.45}
.quote__cite b{font-weight:700}
.photo-round{left:38px;top:250px;width:110px;height:110px;border-radius:50%;border:4px solid var(--ink);background:radial-gradient(circle at 40% 40%,#eef2f6,#8aa3bb)}
</style>
</head>
<body>

<!-- OUTSIDE SPREAD -->
<section class="spread spread--outside">
  <svg class="bg" viewBox="0 0 780 580" aria-hidden="true">
    <defs>
      <linearGradient id="blueGrad" x1="0" y1="0" x2="0" y2="1">
        <stop offset="0" stop-color="#0d5aa6"/><stop offset="1" stop-color="#2f8fe0"/>
      </linearGradient>
      <linearGradient id="mouthGrad" x1="0" y1="0" x2="1" y2="1">
        <stop offset="0" stop-color="#e9c3bf"/><stop offset=".5" stop-color="#c24a57"/><stop offset="1" stop-color="#f3e6e4"/>
      </linearGradient>
    </defs>
    <rect x="0" y="0" width="260" height="580" fill="#fff"/>
    <path d="M0 0H260V30Q110 40 0 150Z" fill="url(#blueGrad)"/>
    <path d="M0 150Q110 40 260 30" fill="none" stroke="#1e1e1e" stroke-width="3"/>
    <path d="M0 440Q160 430 260 330V580H0Z" fill="#6d6e72"/>
    <path d="M0 430Q160 420 260 320" fill="none" stroke="#1e1e1e" stroke-width="4"/>
    <rect x="0" y="572" width="260" height="8" fill="#1b78c8"/>
    <rect x="260" y="0" width="260" height="580" fill="url(#blueGrad)"/>
    <path d="M260 480Q400 470 520 380V580H260Z" fill="#111"/>
    <path d="M260 470Q400 460 520 370" fill="none" stroke="#fff" stroke-width="3"/>
    <rect x="520" y="0" width="260" height="580" fill="#f1f2f4"/>
    <path d="M520 0H780V40Q640 20 520 70Z" fill="url(#blueGrad)"/>
    <path d="M520 70Q640 20 780 40" fill="none" stroke="#1e1e1e" stroke-width="3"/>
    <g role="img" aria-label="Photo: close-up of a smiling mouth with a dental mirror">
      <path d="M520 200Q650 160 780 170V360Q650 400 520 390Z" fill="url(#mouthGrad)"/>
    </g>
    <path d="M520 392Q650 402 780 362" fill="none" stroke="#1b78c8" stroke-width="4"/>
    <rect x="520" y="572" width="260" height="8" fill="#1b78c8"/>
  </svg>

  <div class="abs approval">
    <div class="approval__badge"><span class="sq"></span>KRV MOTO</div>
    <p>Dental Learning Allies, LLC is designated as an Approved KRV MOTO Program Provider by the Keystone Review Voice. The formal continuing education programs of this program provider are accepted by the KRV for Fellowship/Mastership and membership maintenance credit. Approval does not imply acceptance by a state or provincial board of dentistry or KRV endorsement. The current term of approval extends from 07/01/2017 to 06/30/2019. Provider ID #512846</p>
  </div>
  <div class="abs web white" style="left:0;top:500px;width:260px">
    <svg viewBox="0 0 16 16" fill="none" stroke="#fff" stroke-width="1.2"><circle cx="8" cy="8" r="7"/><ellipse cx="8" cy="8" rx="3" ry="7"/><path d="M1 8h14M2.5 4.5h11M2.5 11.5h11"/></svg>
    www.dentallearningallies.example
  </div>

  <div class="abs contact">
    <div class="brand white"><span class="brand__mark"></span>DENTAL LEARNING ALLIES</div>
    <div class="contact__addr">
      <svg viewBox="0 0 14 14" fill="none" stroke="#fff" stroke-width="1.2"><path d="M7 13S2.5 8 2.5 5.2a4.5 4.5 0 0 1 9 0C11.5 8 7 13 7 13Z"/><circle cx="7" cy="5.2" r="1.6"/></svg>
      480 Harbor Line Rd, Suite 12,<br>Bayview, Florida 33000,<br>United States
    </div>
    <div class="person">
      <div class="person__photo" role="img" aria-label="Portrait photo of Nora L. Grant"></div>
      <div class="person__name">Nora L. Grant</div>
      <div class="person__line">&#9742; (555) 014-2281</div>
      <div class="person__line">&#9993; nora@dentallearningallies.example</div>
    </div>
    <div class="person">
      <div class="person__photo" role="img" aria-label="Portrait photo of Paula Dennings"></div>
      <div class="person__name">Paula Dennings</div>
      <div class="person__line">&#9742; (555) 019-7735</div>
      <div class="person__line">&#9993; paula@dentallearningallies.example</div>
    </div>
    <div class="web contact__web">
      <svg viewBox="0 0 16 16" fill="none" stroke="#fff" stroke-width="1.2"><circle cx="8" cy="8" r="7"/><ellipse cx="8" cy="8" rx="3" ry="7"/><path d="M1 8h14M2.5 4.5h11M2.5 11.5h11"/></svg>
      www.dentallearningallies.example
    </div>
  </div>

  <h1 class="abs cover__title">Grow your DSO with customized training solutions</h1>
  <div class="abs brand blue cover__brand"><span class="brand__mark"></span>DENTAL LEARNING ALLIES</div>
</section>

<!-- INSIDE SPREAD -->
<section class="spread spread--inside">
  <svg class="bg" viewBox="0 0 780 580" aria-hidden="true">
    <defs>
      <linearGradient id="blueGrad2" x1="0" y1="0" x2="0" y2="1">
        <stop offset="0" stop-color="#0d5aa6"/><stop offset="1" stop-color="#2f8fe0"/>
      </linearGradient>
      <linearGradient id="roomGrad" x1="0" y1="0" x2="1" y2="1">
        <stop offset="0" stop-color="#e8e4df"/><stop offset=".6" stop-color="#9aa4ae"/><stop offset="1" stop-color="#5c6670"/>
      </linearGradient>
      <linearGradient id="crowdGrad" x1="0" y1="0" x2="1" y2="1">
        <stop offset="0" stop-color="#f4f1ed"/><stop offset=".5" stop-color="#c9b8a6"/><stop offset="1" stop-color="#6f6558"/>
      </linearGradient>
    </defs>
    <path d="M0 0H260V20Q120 20 0 60Z" fill="url(#blueGrad2)"/>
    <path d="M260 0H520V20Q380 15 260 30Z" fill="url(#blueGrad2)"/>
    <path d="M520 0H780V20Q640 15 520 40Z" fill="url(#blueGrad2)"/>
    <g role="img" aria-label="Photo: team meeting around a table with a video call screen">
      <path d="M0 400L250 360L520 440V580H0Z" fill="url(#roomGrad)"/>
    </g>
    <path d="M0 400L250 360L520 440" fill="none" stroke="#1e1e1e" stroke-width="4"/>
    <g role="img" aria-label="Photo: seminar audience raising hands">
      <path d="M520 440V330Q630 270 780 260V580H520Z" fill="url(#crowdGrad)"/>
    </g>
    <rect x="0" y="572" width="780" height="8" fill="#111"/>
  </svg>

  <div class="abs services">
    <h2>Services</h2>
    <ul class="ticks">
      <li>Clinical Training</li>
      <li>Web-Based Learning</li>
      <li>Chairside Coaching</li>
      <li>Train Your Trainer</li>
      <li>Regional or Annual Meetings</li>
      <li>Metric Analytics</li>
    </ul>
  </div>
  <div class="abs photo-round" role="img" aria-label="Photo: trainer holding a clipboard with a colleague"></div>

  <div class="abs why">
    <h2>Why partner with us?</h2>
    <p class="why__lead">Do you want to:</p>
    <ul class="ticks">
      <li>Make hygiene the driver of every dental practice?</li>
      <li>Consistently achieve production goals?</li>
      <li>Provide excellent care for every patient in every practice?</li>
      <li>Provide continuity of care between providers?</li>
      <li>Standardize scripting to increase treatment enrollment?</li>
      <li>Improve the retention of both your staff and your patients?</li>
      <li>Supplement your education initiatives with metrics-based needs assessment?</li>
    </ul>
    <p class="why__cta">If you said yes to any of these questions, then DLA is right for you!</p>
  </div>

  <blockquote class="abs quote">
    <span class="quote__mark quote__mark--open">&ldquo;</span>
    Dental Learning Allies delivered training for our team that isn't offered anywhere else. Their training has dramatically changed our team's ability to influence treatment acceptance. I would recommend their services to any DSO looking to increase profitability!
    <span class="quote__mark quote__mark--close">&rdquo;</span>
  </blockquote>
  <p class="abs quote__cite"><b>Dr. Martin Calloway,</b><br>Chief Clinical Officer,<br>Bright Harbor Practice Group</p>
</section>

</body>
</html>
```